Bellhaven Select Business Card Design Project

About the company: Here at Marigrove Essence, we focus on cosmetic products that based on essential oils and different kinds of plant essences. All of our raw materials are pure organic and specially selected from local producers in Australia.

I'm here to look for a unique business card design, to replace the current one later on, so I don't have many requirements. Why I wanna restrict designers' creativity?

All I know is: 1. do not make it too complicated, straight forward, simple and pure. 2. this design may be used for other purposes (i.e. logo and slogan on the front, Brand Story and contact details at the back). Therefor, I'd like to have the design for 3 layouts, one only have logo, slogan, contact detials, one for the brand story, the other one for the personal business card with staff's mob etc...

A vector graphic is required, i.e. eps, ai, easy for me to resize.

Round Corner.

Thanks
Updates

Plz add "Hand made in Australia" in the design, cheers.

Target Market(s)

Women aged yr 20-50

Industry/Entity Type

Business

Requirements
Must have
• Logo: please see attacment (eps, ai)

Slogan: Dew Touched Delight

Website:www.marigroveessence-demo.com.au

Address: temporary not available

Phone: temporary not available

"Hand made in Australia"

Nice to have
• Prefer round corner

```html
<!DOCTYPE html>
<html lang="en">
<head>
<meta charset="utf-8">
<title>Marigrove Essence — Business Card</title>
<link rel="stylesheet" href="https://fonts.googleapis.com/css2?family=Marcellus&family=Parisienne&family=Open+Sans:wght@400&display=swap">
<style>
  :root {
    --backdrop: #000000;
    --blush-light: #fbe3ec;
    --blush-mid: #f3b3c9;
    --rose: #e6386c;
    --rose-deep: #d8175a;
    --crimson: #f0376a;
    --crimson-deep: #9e1641;
    --ink-rose: #d81d5e;
    --white: #ffffff;
  }
  html, body {
    margin: 0;
    padding: 0;
    width: 1200px;
    height: 900px;
    overflow: hidden;
    background: var(--backdrop);
  }
  .canvas {
    position: relative;
    width: 1200px;
    height: 900px;
    display: flex;
    align-items: center;
    justify-content: center;
    gap: 40px;
  }
  .card {
    position: relative;
    width: 540px;
    height: 310px;
    border-radius: 14px;
    overflow: hidden;
  }
  .card--front {
    background: linear-gradient(180deg, var(--blush-light) 0%, var(--blush-mid) 55%, var(--rose) 85%, var(--rose-deep) 100%);
  }
  .card--back {
    background: linear-gradient(180deg, var(--crimson) 0%, #c51f55 50%, var(--crimson-deep) 100%);
  }
  .rose-backdrop {
    position: absolute;
    left: 110px;
    top: -10px;
    width: 380px;
    height: 340px;
    border-radius: 50%;
    background: radial-gradient(circle at 50% 45%, rgba(255,255,255,0.35) 0%, rgba(255,255,255,0.15) 50%, rgba(255,255,255,0) 72%);
  }
  .brand {
    position: absolute;
    left: 0;
    right: 0;
    top: 92px;
    display: flex;
    align-items: center;
    justify-content: center;
    gap: 12px;
  }
  .brand__mark {
    width: 18px;
    height: 18px;
    border-radius: 50%;
    background: var(--ink-rose);
  }
  .brand__name {
    font-family: "Marcellus", serif;
    font-size: 40px;
    color: var(--ink-rose);
    letter-spacing: 1px;
  }
  .slogan {
    position: absolute;
    left: 0;
    right: 0;
    bottom: 46px;
    text-align: center;
    font-family: "Marcellus", serif;
    font-size: 17px;
    letter-spacing: 1px;
    color: var(--white);
  }
  .tagline {
    position: absolute;
    left: 0;
    right: 0;
    top: 112px;
    text-align: center;
    font-family: "Parisienne", cursive;
    font-size: 32px;
    color: var(--white);
  }
  .website {
    position: absolute;
    left: 0;
    right: 0;
    bottom: 40px;
    text-align: center;
    font-family: "Open Sans", sans-serif;
    font-size: 16px;
    color: var(--white);
  }
</style>
</head>
<body>
  <main class="canvas">
    <section class="card card--front" aria-label="Card front">
      <div class="rose-backdrop" role="img" aria-label="Large faint rose blossom decoration"></div>
      <div class="brand">
        <span class="brand__mark"></span>
        <span class="brand__name">Marigrove Essence</span>
      </div>
      <p class="slogan">DEW TOUCHED DELIGHT</p>
    </section>
    <section class="card card--back" aria-label="Card back">
      <p class="tagline">Hand made in Australia</p>
      <p class="website">www.marigroveessence-demo.com.au</p>
    </section>
  </main>
</body>
</html>
```